Stationary or Corporate Identity package for small Software Development Company

I have a logo and am looking for letterhead, envelope, and possibly business card design. Letterhead and envelope can use all images from the attached business card or open to other ideas that can incorporate the logo. Looking for colorful design to grab attention. Also wanting a more Professional look and less whimsical with maybe a little on the bolder side (maybe more of the masculine side?) Definitely a more modern look over a boring traditional look.

Target Market(s)

Clients are IT Recruiters and IT/Software Staffing and Consulting companies

Industry/Entity Type

Computer Software

Font styles to use
Sans Serif

Requirements
Must have
• Must have the logo, and places for address information, phone number, email, and website information. Colors should coordinate with logo.
Nice to have
• I like the look where there is a semi-transparent abstract image or part of the logo that sort of swooshes in from the left side of the paper. This is not necessary if other good ideas come to mind. Would like a little bit of color to the stationary and envelope, not just a header/footer type with just the logo and a colored separation line.

```html
<!DOCTYPE html>
<html lang="en">
<head>
<meta charset="utf-8">
<title>Vertrix Stationery</title>
<link href="https://fonts.googleapis.com/css2?family=Ubuntu:wght@400;700&family=Tinos&display=swap" rel="stylesheet">
<style>
:root{
  --bg:#eeeeee;
  --paper:#ffffff;
  --ink:#1b1b1b;
  --muted:#555555;
  --navy:#0d3b7a;
  --teal:#145a78;
  --red:#d91f26;
  --green:#3aa935;
  --orange:#f08a1c;
  --yellow:#f5c21a;
  --card-dark:#1e1e1e;
  --mark:#ef6a1e;
}
*{box-sizing:border-box;margin:0;padding:0}
html,body{width:1200px;height:795px;overflow:hidden}
body{background:var(--bg);position:relative;font-family:"Ubuntu",sans-serif;color:var(--ink)}

.letterhead{position:absolute;left:70px;top:45px;width:500px;height:706px;background:var(--paper);box-shadow:0 6px 18px rgba(0,0,0,.12);overflow:hidden}
.brand{position:absolute;display:flex;align-items:center;gap:8px}
.brand-dot{border-radius:50%;background:var(--mark);flex:none}
.brand-text{display:flex;flex-direction:column;line-height:1}
.brand-name{font-family:"Ubuntu",sans-serif;font-weight:700;color:var(--ink)}
.brand-tag{font-family:"Ubuntu",sans-serif;font-weight:400;color:var(--muted);margin-top:2px}

.letterhead .brand{left:190px;top:48px}
.letterhead .brand-dot{width:40px;height:40px}
.letterhead .brand-name{font-size:26px}
.letterhead .brand-tag{font-size:7px;letter-spacing:.3px}

.backdrop-circle{position:absolute;left:270px;top:270px;width:250px;height:250px;border-radius:50%;background:radial-gradient(circle at 45% 45%,rgba(240,120,120,.22),rgba(200,200,200,.16) 70%);}

.letter{position:absolute;left:52px;top:150px;width:380px;font-family:"Tinos",serif;font-size:11.5px;line-height:1.35;color:#222;position:absolute}
.letter p{margin-bottom:13px}
.letter .addr{margin-bottom:13px}
.letter .sign{margin-left:60px}

.letter-footer{position:absolute;left:0;right:0;bottom:24px;text-align:center;font-size:8px;color:var(--muted);line-height:1.6}
.color-band{position:absolute;left:0;right:0;bottom:0;height:10px;display:flex}
.color-band span{display:block;height:100%}
.band-teal{flex:5;background:var(--teal)}
.band-navy{flex:4;background:var(--navy)}
.band-red{flex:.5;background:var(--red)}
.band-green{flex:.5;background:var(--green)}
.band-orange{flex:.5;background:var(--orange)}
.band-yellow{flex:.15;background:var(--yellow)}

.card{position:absolute;width:340px;height:194px;background:var(--paper);box-shadow:0 5px 14px rgba(0,0,0,.14);overflow:hidden}
.card-back{left:700px;top:120px}
.card-front{left:700px;top:420px}

.card-front .brand{left:105px;top:70px}
.card-front .brand-dot{width:44px;height:44px}
.card-front .brand-name{font-size:28px}
.card-front .brand-tag{font-size:7px}

.card-back .brand{left:22px;top:78px}
.card-back .brand-dot{width:30px;height:30px}
.card-back .brand-name{font-size:19px}
.card-back .brand-tag{font-size:5.5px}
.card-panel{position:absolute;inset:0}
.card-contact{position:absolute;right:16px;top:34px;width:150px;color:#eee;font-size:8px;line-height:1.55;text-align:right}
.card-contact .holder{font-size:12px;font-weight:700;margin-bottom:14px;color:#fff}
</style>
</head>
<body>

<section class="letterhead">
  <div class="brand">
    <span class="brand-dot"></span>
    <span class="brand-text"><span class="brand-name">Vertrix</span><span class="brand-tag">Software Development</span></span>
  </div>

  <div class="backdrop-circle" role="img" aria-label="Faint decorative circle"></div>

  <div class="letter">
    <p>Brooklyn, NY 11207<br>June 28, 2007</p>
    <p class="addr">Ms. Marian Holloway<br>Redfield Heritage Fellowship<br>210 Linden Street<br>New York, NY 10014</p>
    <p>Dear Ms. Holloway:</p>
    <p>The Redfield Heritage Fellowship has always loomed on the horizon for me. Ever since I decided to major in history, I have wanted to participate in your program. From the research that I have done, I believe that your program provides its participants with an extensively detailed look at the history of the world through hands-on experience with fossils, artifacts, and other remains that compose the blueprint of our existence. I am applying for the Redfield Heritage Fellowship because I believe that it would benefit me throughout my career and allow me to further understand the ideas behind history and how it is constructed.</p>
    <p>I believe my skills, experience, and goals make me an excellent candidate for your program.</p>
    <p>Thank you very much for considering me for the Redfield Heritage Fellowship. I am looking forward to hearing from you.</p>
    <p class="sign">Sincerely,<br><br>Dana<br>(555) 018-3342</p>
    <p class="sign" style="margin-top:18px">Enclosure</p>
  </div>

  <div class="letter-footer">
    Harbor Lane Dental | Address: 48 Alder Quay Road, Bayfield, County Wexford, Y35 K2P1 | Tel: (01) 470 2213 | Fax: (01) 470 2214<br>
    info@harborlanedental.com | www.harborlanedental.com
  </div>
  <div class="color-band">
    <span class="band-teal"></span><span class="band-navy"></span><span class="band-red"></span><span class="band-green"></span><span class="band-orange"></span><span class="band-yellow"></span>
  </div>
</section>

<section class="card card-back">
  <svg class="card-panel" viewBox="0 0 340 194" width="340" height="194" aria-hidden="true">
    <polygon points="150,0 340,0 340,194 200,194 180,80" fill="var(--card-dark)"/>
    <polygon points="148,60 200,52 196,72 144,80" fill="var(--orange)"/>
  </svg>
  <div class="brand">
    <span class="brand-dot"></span>
    <span class="brand-text"><span class="brand-name">Vertrix</span><span class="brand-tag">Software Development</span></span>
  </div>
  <div class="card-contact">
    <div class="holder">Harbor Lane</div>
    Address: 48 Alder Quay Road<br>
    Bayfield, County Wexford<br>
    Tel: (01) 470 2213<br>
    Fax: (01) 470 2214<br><br>
    info@harborlanedental.com<br>
    www.harborlanedental.com
  </div>
</section>

<section class="card card-front">
  <div class="brand">
    <span class="brand-dot"></span>
    <span class="brand-text"><span class="brand-name">Vertrix</span><span class="brand-tag">Software Development</span></span>
  </div>
</section>

</body>
</html>
```